Letterhead and compliment slip

We are a UK-based market research agency. We are looking for a new letterhead design to incorporate our logo, address details and company information. We are looking for a simple design. It should be modern. It needs to have a qualify feel. As we are UK based it needs to be designed for A4 paper size (letterhead).
I'm really looking for something simple in design terms!
Both letterhead and compliment slip need to include:
Our logo
Company address
Telephone number
Email address
Website address
Company registration number
VAT registration number
Grey and green would be a good colour scheme to fit with our logo

```html
<!DOCTYPE html>
<html lang="en">
<head>
<meta charset="utf-8">
<title>Clearview Insight – Letterhead and Compliment Slip</title>
<link href="https://fonts.googleapis.com/css2?family=Roboto:wght@400;700&family=Questrial&family=Pinyon+Script&display=swap" rel="stylesheet">
<style>
  :root{
    --bg:#dedede;
    --paper:#f7f7f7;
    --green:#9dc33b;
    --grey-text:#555555;
    --grey-dark:#3f3f3f;
    --rule:#9a9a9a;
  }
  *{box-sizing:border-box;margin:0;padding:0}
  html,body{width:1200px;height:1022px;overflow:hidden;background:var(--bg)}
  body{position:relative;font-family:'Questrial',sans-serif;color:var(--grey-text)}

  .brand{display:flex;align-items:center;gap:8px;font-family:'Roboto',sans-serif;font-weight:700;color:var(--green);letter-spacing:-0.5px;white-space:nowrap}
  .brand-dot{border-radius:50%;background:var(--green);flex:none}

  /* Letterhead */
  .letterhead{position:absolute;left:80px;top:75px;width:614px;height:865px;background:var(--paper);overflow:hidden}
  .letterhead .brand{position:absolute;left:0;right:0;top:80px;justify-content:center;font-size:36px}
  .letterhead .brand-dot{width:26px;height:26px}
  .salutation{position:absolute;left:53px;top:240px;font-size:16px;color:var(--grey-dark)}
  .letter-body{position:absolute;left:53px;top:288px;width:512px;font-size:9.3px;line-height:13.2px;color:var(--grey-dark)}
  .letter-body p{margin-bottom:13px}
  .sign-off{position:absolute;left:53px;top:566px;font-size:9.3px;color:var(--grey-dark)}
  .letter-footer{position:absolute;left:0;right:0;top:772px;text-align:center;font-family:'Roboto',sans-serif;font-size:9px;line-height:15px;color:var(--grey-text)}
  .letter-footer .company{color:var(--green)}
  .letter-footer .key{color:var(--green)}
  .letter-footer .sep{margin:0 10px}

  /* Compliment slip */
  .slip{position:absolute;left:511px;top:492px;width:620px;height:281px;background:var(--paper)}
  .slip .brand{position:absolute;left:32px;top:44px;font-size:32px}
  .slip .brand-dot{width:22px;height:22px}
  .slip-address{position:absolute;right:196px;top:42px;text-align:right;font-family:'Roboto',sans-serif;font-size:9px;line-height:12.2px;color:var(--grey-text)}
  .slip-address .company{color:var(--green)}
  .slip-divider{position:absolute;left:437px;top:44px;width:1px;height:46px;background:#d2d2d2}
  .slip-contacts{position:absolute;left:449px;top:44px;list-style:none;font-family:'Roboto',sans-serif;font-size:9px;line-height:12.2px;color:var(--grey-text)}
  .slip-contacts li{display:flex;align-items:center;gap:6px}
  .slip-contacts svg{width:8px;height:8px;fill:var(--green);flex:none}
  .slip-greeting{position:absolute;right:26px;top:186px;font-family:'Pinyon Script',cursive;font-size:40px;color:var(--green);line-height:1}
  .slip-rule{position:absolute;left:32px;top:234px;width:562px;height:1px;background:var(--rule)}
  .slip-reg{position:absolute;left:32px;top:222px;font-family:'Roboto',sans-serif;font-size:9px;line-height:15.5px;color:var(--grey-text)}
</style>
</head>
<body>

<section class="letterhead">
  <div class="brand"><span class="brand-dot"></span>Clearview Insight</div>

  <p class="salutation">Dear Mr. Turner,</p>

  <div class="letter-body">
    <p>Lorem ipsum dolor sit amet, consectetur adipiscing elit. Donec orci purus, luctus vitae dignissim eu, iaculis sed purus. Vivamus faucibus, ipsum nec aliquet viverra, leo mauris condimentum ligula, sit amet sagittis enim ligula quis arcu. Nam egestas tortor id nisi porttitor mattis. In tortor ante, ultricies in suscipit a, tempus non massa. Vivamus et auctor mi. Fusce vel massa nulla. Phasellus nec eros mauris, et scelerisque orci.</p>
    <p>Donec malesuada orci vitae nulla accumsan porta a id massa. Quisque accumsan iaculis magna sit amet fringilla. Maecenas consequat, magna eget tincidunt semper, odio nibh rutrum mi, id feugiat ante nisi eu risus. Vestibulum nunc orci, rhoncus a placerat in, ultricies in mi. Cras mattis varius eros, vel fringilla nisi suscipit eget. Quisque scelerisque sagittis nulla at porttitor.</p>
    <p>Sed id augue vitae urna euismod commodo aliquet a quam. Pellentesque arcu velit, consequat et diam. Nullam erat sem, rhoncus id ullamcorper vitae, rhoncus et arcu. In ut nisi iaculis at. Donec eu magna a metus ornare faucibus. Fusce aliquet faucibus ultricies, idunt gravida, sem arcu adipiscing lacus, ac bibendum nulla leo eu purus. Quisque nec a ccumsan quis quis nibh. Vestibulum id purus lorem.</p>
    <p>It is a long established fact that a reader will be distracted by the readable content of a page when looking at its layout. The point of using Lorem Ipsum is that it has a more-or-less normal distribution of letters, as opposed to using 'Content here, content here', making it look like readable English. Many desktop publishing packages use it.</p>
  </div>

  <p class="sign-off">Sincerely,</p>

  <footer class="letter-footer">
    <div class="company">Clearview Insight Ltd.</div>
    <div>12 Linden Court, Meadow Way, Harpenden, Hertfordshire, AL5 2QT</div>
    <div><span class="key">P:</span> +44 (0)1632 960418 <span class="key">E:</span> hello@clearviewinsight.co.uk <span class="key">W:</span> www.clearviewinsight.co.uk</div>
    <div>Company registration number : 6148207<span class="sep">|</span>VAT registration number : 731205846</div>
  </footer>
</section>

<section class="slip">
  <div class="brand"><span class="brand-dot"></span>Clearview Insight</div>

  <address class="slip-address" style="font-style:normal">
    <div class="company">Clearview Insight Ltd.</div>
    <div>12 Linden Court, Meadow Way</div>
    <div>Harpenden</div>
    <div>Hertfordshire, AL5 2QT</div>
  </address>

  <div class="slip-divider"></div>

  <ul class="slip-contacts">
    <li><svg viewBox="0 0 10 10" aria-hidden="true"><path d="M2 0.5 3.6 2.6 2.7 3.7C3.3 5 4.9 6.7 6.3 7.3L7.4 6.4 9.5 8 8.6 9.5C4.5 9.3 0.7 5.5 0.5 1.4Z"/></svg>+44 (0)1632 960418</li>
    <li><svg viewBox="0 0 10 10" aria-hidden="true"><path d="M0.5 2H9.5V3L5 5.8 0.5 3ZM0.5 4 5 6.8 9.5 4V8.5H0.5Z"/></svg>hello@clearviewinsight.co.uk</li>
    <li><svg viewBox="0 0 10 10" aria-hidden="true"><path d="M5 0.5A4.5 4.5 0 1 0 5 9.5 4.5 4.5 0 1 0 5 0.5ZM2.2 3.2 4.3 3.4 4.8 5 3.6 6.6 2.4 5.6ZM6 2.1 7.8 3.6 7.4 6.6 6 5.4 5.6 3.6Z"/></svg>www.clearviewinsight.co.uk</li>
  </ul>

  <div class="slip-greeting">With Compliments</div>
  <div class="slip-reg">
    <div>VAT registration number : 731205846</div>
    <div>Company registration number : 6148207</div>
  </div>
  <div class="slip-rule"></div>
</section>

</body>
</html>
```